Halvory Professional Services Website

Small website for company presence and information. Company is an IT/Telecom services company. We provide presales and installation services. Included are various company logos including color levels. Site doesn't have to use these exact colors in the logos, but should be complimentary if using different colors. It should have a professional business appearance.
Updates

My apologies for not being more responsive on the designs that have been submitted. I will be narrowing down the submissions and providing additional feedback next week. Thank you for your patience.

Project Deadline Extended
Reason: Sorry again for delays on picking designs. Work has me very busy and I've just not had the time to devote to this project. I am extending the design deadline for a few more days to give me time to make my final decisions. Thank you all for your patience. Stay tuned....

Target Market(s)

Telecom sales companies that sell Brintel telecom products.

Industry/Entity Type

Professional Service

Coding

Coded - Design and coding required

Number of Pages Required

5+ page

Font styles to use
Sans Serif

Colors
3276b5
0355a3
85abd2
85cae6
33a6d7
0692cd
ffffff

Requirements
Must have
• Professional design reflective of IT/Telecom business. A good reference website would be: http://www.quollanetworks.example/. Looking for something similar in function and presence.
Nice to have
• Rolling photos highlighting our services. Traditional navigation across the top of all pages.
Should not have
• No motion video, flashy presentation or overly confused interface.

```html
<!DOCTYPE html>
<html lang="en">
<head>
<meta charset="utf-8">
<title>Halvory Professional Services</title>
<link rel="stylesheet" href="https://fonts.googleapis.com/css2?family=Open+Sans:ital,wght@0,300;0,400;0,600;0,700;1,400;1,600;1,700&display=swap">
<style>
:root{
  --navy:#1b2c66;
  --navy-deep:#14214f;
  --navy-band:#1f3275;
  --blue:#3276b5;
  --sky:#33a6d7;
  --cyan:#00b4ee;
  --orange:#f7a21b;
  --ink:#333a44;
  --muted:#555c66;
  --soft:#f2f2f2;
  --white:#ffffff;
}
*{box-sizing:border-box;margin:0;padding:0}
html,body{width:1200px;height:3000px;overflow:hidden}
body{font-family:"Open Sans",Arial,sans-serif;color:var(--ink);background:var(--white);position:relative}
section,header,footer{position:absolute;left:0;width:1200px}
ul{list-style:none}

/* header */
.site-header{top:0;height:52px;background:var(--navy)}
.brand{position:absolute;left:170px;top:10px;display:flex;align-items:center;gap:10px;color:var(--white)}
.brand-mark{width:26px;height:26px;border:2px solid var(--white);border-radius:50%}
.brand-name{font-size:19px;font-weight:700;letter-spacing:1px;line-height:1}
.brand-sub{font-size:7px;font-weight:700;letter-spacing:.6px;text-transform:uppercase;display:block;margin-top:3px}
.main-nav{position:absolute;right:168px;top:0;display:flex;gap:40px;height:52px;align-items:center}
.main-nav a{color:var(--white);font-size:11px;text-decoration:none;text-transform:uppercase}

/* hero */
.hero{top:52px;height:446px;background:linear-gradient(90deg,#f3f3f4 0%,#e6e7e9 55%,#d7d8db 100%)}
.hero-title{position:absolute;left:170px;top:150px;font-size:30px;font-style:italic;font-weight:700;color:var(--navy)}
.hero-title span{color:var(--sky)}
.hero-text{position:absolute;left:170px;top:198px;width:400px;font-size:19px;font-style:italic;line-height:29px;color:#333}
.hero-cta{position:absolute;left:170px;top:280px;display:flex;height:44px}
.hero-cta .cta-arrow{width:40px;background:var(--white);display:flex;align-items:center;justify-content:center}
.hero-cta .cta-label{background:var(--orange);color:var(--navy);font-weight:700;font-size:18px;padding:0 14px;display:flex;align-items:center}
.hero-art{position:absolute;left:560px;top:0}
.slide-arrow{position:absolute;top:206px}
.slide-prev{left:30px}.slide-next{right:30px}

/* intro */
.intro{top:498px;height:350px;text-align:center}
.intro h2{position:absolute;left:200px;top:64px;width:800px;font-size:23px;font-weight:400;line-height:30px;color:#222}
.intro .lead{position:absolute;left:260px;top:138px;width:680px;font-size:13px;line-height:21px;color:var(--muted)}
.intro h3{position:absolute;left:0;top:210px;width:1200px;font-size:15px;font-weight:600;color:#222}
.intro .note{position:absolute;left:330px;top:244px;width:540px;font-size:13px;line-height:21px;color:var(--muted)}

/* band */
.band{top:848px;height:444px;background:var(--navy-band)}
.band h2{position:absolute;left:170px;top:68px;width:460px;font-size:22px;font-weight:300;line-height:30px;color:var(--sky)}
.band-list{position:absolute;left:170px;top:180px;width:412px}
.band-list li{position:relative;padding-left:14px;font-size:13px;line-height:20px;color:var(--white);margin-bottom:16px}
.band-list li::before{content:"›";position:absolute;left:0;top:-1px;font-size:16px}
.band-photo{position:absolute;left:684px;top:32px;width:352px;height:352px;border-radius:50%;border:4px solid var(--white);background:radial-gradient(circle at 50% 40%,#c9a48c 0%,#a7b9cf 45%,#dfe6ee 100%)}

/* features */
.features{top:1292px;height:418px;text-align:center}
.features h2{position:absolute;left:0;top:76px;width:1200px;font-size:23px;font-weight:400;color:var(--sky)}
.features .sub{position:absolute;left:0;top:116px;width:1200px;font-size:13px;color:var(--muted)}
.feature{position:absolute;top:184px;width:260px}
.feature svg{display:block;margin:0 auto}
.feature h3{font-size:16px;font-weight:400;color:#333;margin-top:20px}
.feature p{font-size:13px;line-height:26px;color:var(--muted);margin-top:12px}

/* split */
.split{top:1710px;height:496px;background:var(--soft);overflow:hidden}
.split-photo{position:absolute;left-:0;left:-350px;top:-100px;width:790px;height:700px;border-radius:50%;border:5px solid #c5d4e3;background:radial-gradient(circle at 60% 45%,#d8b99a 0%,#a9886a 35%,#54463d 80%)}
.split-body{position:absolute;left:480px;top:62px;width:540px}
.split-body h2{font-size:21.5px;font-weight:400;line-height:31px;color:#222}
.split-body .lead{font-size:13px;line-height:21px;color:var(--muted);margin-top:8px;width:530px}
.split-list{margin-top:19px;width:530px}
.split-list li{position:relative;padding-left:20px;font-size:12px;line-height:20px;color:var(--navy);margin-bottom:18px}
.split-list li::before{content:"›";position:absolute;left:0;top:-2px;font-size:16px}
.btn-orange{display:inline-block;background:var(--orange);color:var(--navy);font-weight:700;font-size:18px;padding:10px 16px;text-transform:uppercase}
.split .btn-orange{margin-top:12px}

/* cards */
.cards{top:2206px;height:268px;text-align:center}
.card{position:absolute;top:50px;width:260px}
.card svg{display:block;margin:0 auto}
.card h3{font-size:23px;font-weight:400;color:var(--sky);margin-top:2px;line-height:30px}
.card p{font-size:13px;line-height:21px;color:var(--muted);margin-top:6px}
.btn-cyan{display:inline-block;margin-top:18px;background:var(--cyan);color:var(--white);font-weight:700;font-size:13px;padding:9px 16px;text-transform:uppercase}

/* footer */
.site-footer{top:2474px;height:526px;background:linear-gradient(120deg,var(--navy-deep) 0%,#172a68 50%,#1e3a8c 100%);overflow:hidden;color:var(--white)}
.footer-shapes{position:absolute;left:0;top:0}
.footer-col{position:absolute;top:58px}
.footer-col h4{font-size:19px;font-weight:400;text-transform:uppercase}
.footer-col h4::after{content:"";display:block;width:30px;height:2px;background:var(--white);margin-top:8px}
.footer-col ul{margin-top:16px}
.footer-col li{font-size:11px;line-height:21px}
.footer-cta{position:absolute;right:168px;top:318px;text-align:right}
.footer-cta p{font-size:14px;font-weight:600;letter-spacing:.5px;text-transform:uppercase}
.footer-cta .btn-orange{margin-top:12px;font-size:19px;padding:8px 18px}
.footer-rule{position:absolute;left:170px;top:416px;width:862px;height:1px;background:rgba(255,255,255,.25)}
.legal{position:absolute;left:170px;top:436px;font-size:10px;line-height:21px}
.social{position:absolute;right:168px;top:458px;display:flex;gap:20px}
.social span{width:28px;height:28px;border-radius:50%;background:#2a4a9f;display:block}
</style>
</head>
<body>

<header class="site-header">
  <div class="brand">
    <span class="brand-mark"></span>
    <div><span class="brand-name">HALVORY</span><span class="brand-sub">Professional Services</span></div>
  </div>
  <nav class="main-nav">
    <a href="#">Home</a><a href="#">Company</a><a href="#">Services</a><a href="#">Support</a><a href="#">Contact Us</a>
  </nav>
</header>

<section class="hero">
  <svg class="slide-arrow slide-prev" width="20" height="34" viewBox="0 0 20 34"><path d="M16 3 3 17l13 14" fill="none" stroke="#3276b5" stroke-width="4"/></svg>
  <svg class="slide-arrow slide-next" width="20" height="34" viewBox="0 0 20 34"><path d="M4 3l13 14L4 31" fill="none" stroke="#3276b5" stroke-width="4"/></svg>
  <h1 class="hero-title"><span>Lorem ipsum</span> dolor sit amet</h1>
  <p class="hero-text">consectetur adipiscing elit, sed do eiusmod tempor incididunt ut labore et dolore.</p>
  <div class="hero-cta">
    <span class="cta-arrow"><svg width="24" height="24" viewBox="0 0 24 24"><circle cx="12" cy="12" r="11" fill="#1b2c66"/><path d="M6 12h10M12 7l5 5-5 5" fill="none" stroke="#fff" stroke-width="2.4"/></svg></span>
    <span class="cta-label">LEARN MORE</span>
  </div>
  <svg class="hero-art" width="500" height="446" viewBox="0 0 500 446">
    <path d="M140 150 L100 290" stroke="#3276b5" stroke-width="2"/>
    <path d="M190 130 L230 180" stroke="#3276b5" stroke-width="2"/>
    <path d="M148 330 L190 315" stroke="#3276b5" stroke-width="2"/>
    <circle cx="152" cy="98" r="58" fill="#fff" stroke="#3276b5" stroke-width="3"/>
    <circle cx="152" cy="98" r="52" fill="#8d7b6c" role="img" aria-label="Photo of a smiling professional"/>
    <circle cx="336" cy="278" r="150" fill="#fff" stroke="#3276b5" stroke-width="3"/>
    <circle cx="336" cy="278" r="142" fill="#c7ced8" role="img" aria-label="Photo of a team meeting in a bright conference room"/>
    <circle cx="90" cy="342" r="60" fill="#fff" stroke="#3276b5" stroke-width="3"/>
    <circle cx="90" cy="342" r="54" fill="#9c8575" role="img" aria-label="Photo of colleagues collaborating"/>
  </svg>
</section>

<section class="intro">
  <h2>It is a long established fact that a reader will be distracted by the readable content of a page when looking at its layout.</h2>
  <p class="lead">Lorem Ipsum is simply dummy text of the printing and typesetting industry. Lorem Ipsum has been the industry's standard dummy text ever since the 1500s, when an unknown printer took a galley of type and scrambled it to make a type specimen book.</p>
  <h3>The standard Lorem Ipsum passage, used since the 1500s</h3>
  <p class="note">Lorem Ipsum is simply dummy text of the printing and typesetting industry. Lorem Ipsum has been the industry's standard dummy text ever since the</p>
</section>

<section class="band">
  <h2>It is a long established fact that a reader will be distracted by the readable content of a page when looking at its layout.</h2>
  <ul class="band-list">
    <li>Lorem Ipsum is simply dummy text of the printing and typeset industry. Lorem Ipsum has been the industry's standard dummy text ever since the 1500s, when an unknown.</li>
    <li>Lorem Ipsum is simply dummy text of the printing and typeset industry. Industry's standard dummy text ever since the 1500s, when an unknown.</li>
    <li>Lorem Ipsum is simply dummy text of the printing and typeset industry. Lorem Ipsum has been the industry's standard.</li>
  </ul>
  <div class="band-photo" role="img" aria-label="Photo of a smiling woman holding a tablet"></div>
</section>

<section class="features">
  <h2>It is a long established fact that a reader will be</h2>
  <p class="sub">Lorem Ipsum is simply dummy text of the printing</p>
  <div class="feature" style="left:174px">
    <svg width="48" height="50" viewBox="0 0 48 50"><path d="M24 2 44 9v14c0 13-9 22-20 26C13 45 4 36 4 23V9z" fill="#00b4ee"/><path d="M24 2v24H4V9zM24 26h20c0 11-9 19-20 23z" fill="#fff" opacity=".85"/></svg>
    <h3>Income Guarantee</h3>
    <p>Lorem Ipsum is simply dummy text<br>of the printing and typesetting.</p>
  </div>
  <div class="feature" style="left:470px">
    <svg width="52" height="50" viewBox="0 0 52 50"><path d="M6 10 34 4l3 8" fill="none" stroke="#00b4ee" stroke-width="4"/><rect x="4" y="14" width="42" height="30" rx="3" fill="#00b4ee"/><rect x="32" y="24" width="16" height="10" rx="2" fill="#fff"/><circle cx="38" cy="29" r="2.5" fill="#00b4ee"/></svg>
    <h3>Cash Boosts</h3>
    <p>Lorem Ipsum is simply dummy text<br>of the printing and typesetting.</p>
  </div>
  <div class="feature" style="left:766px">
    <svg width="52" height="50" viewBox="0 0 52 50"><rect x="4" y="14" width="44" height="10" fill="#00b4ee"/><rect x="8" y="26" width="36" height="22" fill="#00b4ee"/><rect x="23" y="14" width="6" height="34" fill="#fff"/><path d="M26 13c-4-9-14-10-14-4s10 4 14 4zM26 13c4-9 14-10 14-4s-10 4-14 4z" fill="none" stroke="#00b4ee" stroke-width="3"/></svg>
    <h3>Peace of Mind</h3>
    <p>Lorem Ipsum is simply dummy text<br>of the printing and typesetting.</p>
  </div>
</section>

<section class="split">
  <div class="split-photo" role="img" aria-label="Photo of a smiling businesswoman in a meeting"></div>
  <div class="split-body">
    <h2>Sed ut perspiciatis unde omnis iste natus error sit volup tatem accusantium doloremque laudantium.</h2>
    <p class="lead">Lorem Ipsum is simply dummy text of the printing and typesetting industry. Lorem Ipsum has been the industry's standard dummy text ever since the 1500s, when an unknown printer took a galley of type and scrambled.</p>
    <ul class="split-list">
      <li>Lorem Ipsum is simply dummy text of the printing and typeset industry. Lorem Ipsum has been the industry's standard dummy text ever since the</li>
      <li>"But I must explain to you how all this mistaken idea of denouncing pleasure and praising pain was born and I will give you a complete account actual teachings.</li>
      <li>Lorem Ipsum is simply dummy text of the printing and typeset industry. Lorem Ipsum has been the industry's standard dummy text ever since the</li>
    </ul>
    <span class="btn-orange">Get Started Today!</span>
  </div>
</section>

<section class="cards">
  <div class="card" style="left:182px">
    <svg width="36" height="32" viewBox="0 0 36 32"><rect x="2" y="5" width="32" height="22" fill="none" stroke="#00b4ee" stroke-width="3"/><rect x="7" y="10" width="10" height="8" fill="#00b4ee"/><path d="M20 11h10M20 16h10M7 22h23" stroke="#00b4ee" stroke-width="2"/></svg>
    <h3>News</h3>
    <p>Lorem Ipsum is simply dummy text<br>of the printing and typesetting.</p>
    <span class="btn-cyan">Learn More</span>
  </div>
  <div class="card" style="left:468px">
    <svg width="32" height="32" viewBox="0 0 32 32"><rect x="3" y="6" width="26" height="24" fill="none" stroke="#00b4ee" stroke-width="3"/><rect x="3" y="6" width="26" height="6" fill="#00b4ee"/><path d="M9 2v7M23 2v7" stroke="#00b4ee" stroke-width="3"/><path d="M8 16h4M14 16h4M20 16h4M8 21h4M14 21h4M20 21h4M8 26h4M14 26h4" stroke="#00b4ee" stroke-width="3"/></svg>
    <h3>Events</h3>
    <p>Lorem Ipsum is simply dummy text<br>of the printing and typesetting.</p>
    <span class="btn-cyan">Learn More</span>
  </div>
  <div class="card" style="left:758px">
    <svg width="36" height="32" viewBox="0 0 36 32"><circle cx="8" cy="9" r="4" fill="#00b4ee"/><circle cx="28" cy="9" r="4" fill="#00b4ee"/><circle cx="18" cy="10" r="6" fill="#00b4ee"/><path d="M1 23c0-6 3-9 7-9s7 3 7 9zM21 23c0-6 3-9 7-9s7 3 7 9zM8 30c0-8 4-13 10-13s10 5 10 13z" fill="#00b4ee"/></svg>
    <h3>Partners</h3>
    <p>Lorem Ipsum is simply dummy text<br>of the printing and typesetting.</p>
    <span class="btn-cyan">Learn More</span>
  </div>
</section>

<footer class="site-footer">
  <svg class="footer-shapes" width="1200" height="526" viewBox="0 0 1200 526">
    <path d="M880 0 1200 420V0z" fill="#2450b0" opacity=".35"/>
    <path d="M1200 100 700 526h500z" fill="#1b3c94" opacity=".4"/>
    <path d="M0 200 300 526H0z" fill="#0f1a42" opacity=".5"/>
  </svg>
  <div class="footer-col" style="left:170px">
    <h4>Companies</h4>
    <ul><li>Quolla Leasing</li><li>Quolla IT Inc.</li><li>Quolla IT United Kingdom</li><li>Tessel AG</li><li>Quolla IT Australia</li><li>Quolla IT Singapore</li><li>Quolla IT India</li><li>Quolla IT Hong Kong</li><li>Quolla IT China</li></ul>
  </div>
  <div class="footer-col" style="left:390px">
    <h4>About Us</h4>
    <ul><li>About Quolla IT</li><li>About Quolla Group</li><li>Careers</li><li>Leadership</li><li>Locations</li><li>Resources</li><li>News</li></ul>
  </div>
  <div class="footer-col" style="left:602px">
    <h4>Competencies</h4>
    <ul><li>Data Center Solutions</li><li>Unified Workspace</li><li>Cloud Services</li><li>Security &amp; Risk Management</li></ul>
  </div>
  <div class="footer-col" style="left:818px">
    <h4>Services</h4>
    <ul><li>Implementation and Integration</li><li>Infrastructure Cabling</li><li>Managed Services</li><li>Network Operations Center (NOC)</li><li>Readiness Assessment</li><li>Refurbished Equipment and Buyback</li></ul>
  </div>
  <div class="footer-cta">
    <p>Let's continue the conversation.</p>
    <span class="btn-orange">Contact Us</span>
  </div>
  <div class="footer-rule"></div>
  <div class="legal">
    <p>©2017 Halvory Professional Services</p>
    <p>A Quolla Group International Company</p>
    <p>Privacy/Cookie Policy / Safe Harbor Policy</p>
  </div>
  <div class="social"><span></span><span></span><span></span><span></span></div>
</footer>

</body>
</html>
```